Local Service Business Needing Clear Business Card Design

We are needing a business card design to be made for our power washing company. Business cards will be printed on plastic standard sized cards. We're looking for someone who can make a unique and unforgettable design. Double sided and or single sided concepts would be ideal. Of course keeping in mind we are seeking translucent cards but not married to the idea of having them as the main concern is just to have plastic cards to prevent water damage! :D

More info on our company can be found on brightlakesurfacecare.example

Not looking for a list of our services. Simply applying company info and possibly "Commercial Residential Fleet" on them tastefully and appropriate to design is all thats needed.

Phone number for our company is 877-RNS-CREW or 877-736-2739

Industry/Entity Type

Power Washing

Contact Information for Business Card

Phone, Web URL,

Requirements
Should not have
• Bubbles, water or super distracting graphics. Looking for a simple and clean look. Unfortunately our logo is this way which we may seek to change in the near future.

```html
<!DOCTYPE html>
<html lang="en">
<head>
<meta charset="utf-8">
<title>Bright Lake Surface Care – Business Card</title>
<link rel="stylesheet" href="https://fonts.googleapis.com/css2?family=Arimo:wght@400;700&display=swap">
<style>
  :root {
    --backdrop: #9aabb9;
    --card-edge: #e4eef5;
    --card-light: #d3e1ec;
    --card-mid: #b9c9d6;
    --accent-blue: #1a9ad6;
    --ink: #161a1e;
    --rule: #111417;
  }
  * { margin: 0; padding: 0; box-sizing: border-box; }
  html, body {
    width: 1200px;
    height: 927px;
    overflow: hidden;
    background: var(--backdrop);
    font-family: "Arimo", Arial, sans-serif;
  }
  .business-card {
    position: absolute;
    left: 50px;
    top: 149px;
    width: 1100px;
    height: 629px;
    border-radius: 34px;
    border: 2px solid var(--card-edge);
    background: radial-gradient(ellipse at 28% 45%, var(--card-light) 0%, var(--card-mid) 70%, #afc1cf 100%);
    color: var(--ink);
  }
  .company-name {
    position: absolute;
    right: 72px;
    top: 110px;
    text-align: right;
    font-weight: 700;
    font-size: 44px;
    line-height: 1.12;
    color: var(--accent-blue);
    display: flex;
    align-items: center;
    gap: 18px;
  }
  .company-mark {
    width: 26px;
    height: 26px;
    border-radius: 50%;
    background: var(--accent-blue);
    flex: none;
  }
  .person-name {
    position: absolute;
    left: 75px;
    top: 325px;
    font-size: 37px;
    font-weight: 700;
    color: var(--accent-blue);
  }
  .person-title {
    position: absolute;
    left: 75px;
    top: 372px;
    font-size: 28px;
  }
  .divider {
    position: absolute;
    left: 75px;
    top: 415px;
    width: 953px;
    height: 2px;
    background: var(--rule);
  }
  .contact-list {
    position: absolute;
    left: 75px;
    top: 444px;
    list-style: none;
    font-size: 29px;
    line-height: 36px;
  }
  .contact-list li { display: flex; align-items: center; gap: 14px; }
  .contact-icon { width: 26px; height: 26px; flex: none; fill: var(--accent-blue); }
  .address {
    position: absolute;
    right: 72px;
    top: 444px;
    text-align: right;
    font-size: 29px;
    line-height: 36px;
    font-style: normal;
  }
</style>
</head>
<body>
  <section class="business-card">
    <div class="company-name">
      <span class="company-mark"></span>
      <span>Bright Lake<br>Surface Care</span>
    </div>

    <h1 class="person-name">Daniel Harper</h1>
    <p class="person-title">Manager</p>
    <div class="divider"></div>

    <ul class="contact-list">
      <li>
        <svg class="contact-icon" viewBox="0 0 24 24" aria-hidden="true"><path d="M6.6 10.8a15.1 15.1 0 0 0 6.6 6.6l2.2-2.2c.3-.3.7-.4 1-.2 1.1.4 2.3.6 3.6.6.6 0 1 .4 1 1V20c0 .6-.4 1-1 1A17 17 0 0 1 3 4c0-.6.4-1 1-1h3.5c.6 0 1 .4 1 1 0 1.3.2 2.5.6 3.6.1.3 0 .7-.2 1z"/></svg>
        <span>877-RNS-CREW</span>
      </li>
      <li>
        <svg class="contact-icon" viewBox="0 0 24 24" aria-hidden="true"><path d="M2 5h20v14H2z M2 5l10 8 10-8" fill="none" stroke="#1a9ad6" stroke-width="2"/><path d="M2 5h20l-10 8z"/></svg>
        <span>info@brightlakesurfacecare.example</span>
      </li>
      <li>
        <svg class="contact-icon" viewBox="0 0 24 24" aria-hidden="true"><circle cx="12" cy="12" r="10" fill="none" stroke="#1a9ad6" stroke-width="2"/><path d="M2 12h20M12 2c3 3 3 17 0 20M12 2c-3 3-3 17 0 20" fill="none" stroke="#1a9ad6" stroke-width="2"/></svg>
        <span>brightlakesurfacecare.example</span>
      </li>
    </ul>

    <address class="address">
      2280 Alder Ave.<br>
      Fenwick, MI 48832
    </address>
  </section>
</body>
</html>
```